Promotion for a play Eqpt. company

We are looking for a postcard/flyer design to be used at a business to business conference for Airport executives, topic being 'customer service'. We are specialty playground equipment company. This is a pilot program for us, to introduce the concept of installing our equipment in airport settings. It MUST have a VERY professional/corporate feel, while not "losing face" of it being about fun and play.

Our company name is "BrambleNest". The product we offer is a completely custom, "turnkey" environment, completely adaptable to all needs and amenities incl. electronic components. Additionally, they are highly creative, colorful, ultra safe and long lasting. The ideas that we would like to convey are,
#1. This is the future of (commercial) play grounds("embracing the future").
#2. The growing trend in customer service; an amenity that the forward/modern Airport cannot do without.
#3. This is a powerful vehicle for driving advertising dollars.
#4. "Lets talk", we want to listen to your needs and challenges and learn how we can best service you
Updates

Target Market(s)

Business Executives

Industry/Entity Type

Advertising

Requirements
Must have
• Listed above.
Will prob have to crop photos to achieve maximum presentability.

Contact info: www.bramblenest-example.com
800.71.PLUMS
732.908.1357
info@bramblenest-example.com
Nice to have
• Perhaps could contain a "stock photo" like image of something like two business people(woman and man) shaking hands....conveying idea of this being a business advantage, beyond merely "fun and play"
#1. This is the future of (commercial) play grounds("embracing the future")/ The growing trend in customer service; an amenity that the forward/modern Airport cannot do without.
#2. This is a powerful vehicle for driving advertising dollars/this is a revenue DRIVING amenity.
#3. "Lets talk", we want to listen to your needs and challenges and learn how we can best service you
#4. We are turnkey providers.

```html
<!DOCTYPE html>
<html lang="en">
<head>
<meta charset="utf-8">
<title>BrambleNest – Fun &amp; Play Flyer</title>
<link rel="stylesheet" href="https://fonts.googleapis.com/css2?family=Fredoka:wght@600&family=Archivo+Black&family=Open+Sans:ital,wght@1,800&family=Arimo:wght@400;700&display=swap">
<style>
  :root {
    --stage: #5f6062;
    --sky-top: #45a6e2;
    --sky-bottom: #c6e6f8;
    --paper: #ffffff;
    --navy: #1a4b9c;
    --tag-blue: #213d8c;
    --red: #e3204c;
    --pink: #e8168c;
    --yellow: #ffe81a;
    --orange: #f6a11f;
    --ink: #2a2a2a;
    --t-teal: #19b0c9;
    --t-indigo: #5557a8;
    --t-red: #ea4a5e;
    --t-blue: #1f5aa0;
    --t-green: #17a64a;
    --t-pink: #ea4b9a;
    --t-lime: #a7cf67;
    --t-purple: #a3288c;
  }
  * { margin: 0; padding: 0; box-sizing: border-box; }
  html, body { width: 962px; height: 1200px; overflow: hidden; background: var(--stage); }
  .canvas { position: relative; width: 962px; height: 1200px; }
  .flyer {
    position: absolute; left: 83px; top: 85px; width: 797px; height: 1032px;
    overflow: hidden;
    background: linear-gradient(180deg, var(--sky-top) 0%, #7cc2ec 40%, var(--sky-bottom) 85%);
  }
  .sky-glow {
    position: absolute; inset: 0;
    background:
      radial-gradient(ellipse 260px 90px at 120px 330px, rgba(255,255,255,.75), transparent 70%),
      radial-gradient(ellipse 320px 110px at 560px 520px, rgba(255,255,255,.7), transparent 70%),
      radial-gradient(ellipse 300px 90px at 300px 140px, rgba(255,255,255,.45), transparent 70%),
      radial-gradient(ellipse 280px 120px at 700px 780px, rgba(255,255,255,.55), transparent 70%);
  }
  .ground { position: absolute; left: 0; top: 0; width: 797px; height: 1032px; }
  .title { position: absolute; left: 0; top: 0; width: 797px; height: 220px;
    filter: drop-shadow(3px 5px 4px rgba(0,0,0,.25)); }
  .title text { font-family: "Fredoka", "Arial Rounded MT Bold", sans-serif; font-weight: 600;
    stroke: #fff; stroke-width: 14px; stroke-linejoin: round; paint-order: stroke; }
  .headline { position: absolute; right: 54px; text-align: right;
    font-family: "Archivo Black", "Arial Black", sans-serif; text-transform: uppercase;
    text-shadow: 0 0 6px #fff, 0 0 10px #fff; line-height: 1; }
  .headline--future { top: 211px; font-size: 34px; color: var(--navy); letter-spacing: 1px; }
  .headline--grounds { top: 250px; font-size: 46px; color: var(--red); letter-spacing: 1px; }
  .tagline { position: absolute; right: 44px; top: 318px; width: 600px; text-align: right;
    font-family: "Open Sans", Verdana, sans-serif; font-style: italic; font-weight: 800;
    font-size: 25px; line-height: 32px; color: var(--tag-blue); white-space: nowrap; }
  .aircraft-placeholder { position: absolute; left: 46px; top: 282px; width: 208px; height: 66px;
    border-radius: 33px;
    background: linear-gradient(180deg, rgba(255,255,255,.85) 0%, rgba(216,221,227,.75) 100%); }
  .photo { position: absolute; background: var(--paper); padding: 10px;
    box-shadow: 3px 5px 10px rgba(0,0,0,.35); }
  .photo__image { width: 100%; height: 100%; }
  .photo--butterfly { left: 7px; top: 395px; width: 380px; height: 270px; transform: rotate(9deg); }
  .photo--butterfly .photo__image {
    background: linear-gradient(135deg, #6a5a3a 0%, #b9a15a 30%, #7ea552 55%, #2c3f86 80%, #cbb69a 100%); }
  .photo--playfloor { left: 87px; top: 625px; width: 392px; height: 272px; transform: rotate(-6deg); }
  .photo--playfloor .photo__image {
    background: linear-gradient(160deg, #4a2a26 0%, #a37b45 25%, #2f4a96 45%, #6ea65a 65%, #c2a47a 85%, #d23a30 100%); }
  .pitch { position: absolute; left: 472px; top: 438px; width: 320px; height: 390px;
    transform: rotate(6deg); background: var(--pink);
    box-shadow: 3px 5px 10px rgba(0,0,0,.3);
    padding: 34px 10px 0 10px; text-align: center;
    font-family: "Arimo", Arial, sans-serif; font-weight: 700; font-size: 21px; line-height: 23px;
    color: #fff; white-space: nowrap; }
  .pitch p + p { margin-top: 32px; }
  .pitch .accent { color: var(--yellow); }
  .order-badge { position: absolute; left: 27px; top: 750px; width: 162px; height: 162px;
    border-radius: 50%; background: var(--orange); border: 4px solid #fff;
    display: flex; align-items: center; justify-content: center; text-align: center;
    box-shadow: 2px 4px 8px rgba(0,0,0,.3); }
  .order-badge span { transform: rotate(-22deg); font-family: "Archivo Black", "Arial Black", sans-serif;
    font-size: 31px; line-height: 34px; color: #fff; }
  .contact { position: absolute; left: 37px; top: 945px; font-style: normal;
    font-family: "Arimo", Arial, sans-serif; color: var(--pink); }
  .contact__phone { font-size: 36px; line-height: 40px; }
  .contact__web { font-size: 21px; line-height: 26px; margin-top: 4px; }
  .brand { position: absolute; right: 45px; top: 952px; display: flex; align-items: center; gap: 12px; }
  .brand__dot { width: 26px; height: 26px; border-radius: 50%; background: var(--t-purple); }
  .brand__name { font-family: "Arimo", Arial, sans-serif; font-weight: 700; font-size: 46px;
    line-height: 1; color: var(--ink); letter-spacing: -1px; }
</style>
</head>
<body>
<main class="canvas">
  <article class="flyer">
    <div class="sky-glow"></div>

    <svg class="ground" viewBox="0 0 797 1032" aria-hidden="true">
      <path d="M0 895 Q 420 880 797 858 L797 1032 L0 1032 Z" fill="#ffffff"/>
    </svg>

    <svg class="title" viewBox="0 0 797 220">
      <text x="38" y="180" font-size="172" textLength="720" lengthAdjust="spacingAndGlyphs">
        <tspan fill="var(--t-teal)">F</tspan><tspan fill="var(--t-indigo)">U</tspan><tspan fill="var(--t-red)">N</tspan><tspan fill="var(--t-blue)" font-size="118"> &amp; </tspan><tspan fill="var(--t-green)">P</tspan><tspan fill="var(--t-pink)">L</tspan><tspan fill="var(--t-lime)">A</tspan><tspan fill="var(--t-purple)">Y</tspan>
      </text>
    </svg>

    <h1 class="headline headline--future">Embracing the Future</h1>
    <h2 class="headline headline--grounds">Play Grounds</h2>

    <div class="aircraft-placeholder" role="img" aria-label="Illustration of a passenger jet flying across the sky"></div>

    <p class="tagline">The growing trend in customer<br>service; an amenity that the forward/<br>modern Airport cannot do without.</p>

    <figure class="photo photo--butterfly">
      <div class="photo__image" role="img" aria-label="Photo of a child on a colourful butterfly play structure in an indoor play area"></div>
    </figure>
    <figure class="photo photo--playfloor">
      <div class="photo__image" role="img" aria-label="Photo of children playing on soft play pieces and a toy car in a mall play zone"></div>
    </figure>

    <section class="pitch">
      <p>This is a powerful<br>vehicle for driving<br>advertising dollars/<br>this is a revenue<br><span class="accent">DRIVING</span> amenity.</p>
      <p><span class="accent">"Lets talk",</span> we want to<br>listen to your needs<br>and challenges and<br>learn how we can best<br>service you</p>
    </section>

    <div class="order-badge"><span>ORDER<br>NOW!!</span></div>

    <address class="contact">
      <div class="contact__phone">CALL: 732.908.1357</div>
      <div class="contact__web">WWW.BRAMBLENEST-EXAMPLE.COM</div>
    </address>

    <div class="brand">
      <span class="brand__dot"></span>
      <span class="brand__name">BrambleNest</span>
    </div>
  </article>
</main>
</body>
</html>
```